E-Liquid Bottle Labels

We are looking to redesign the label on our e-cigarette juice bottles.

We are trying to brand our company "Copper Lantern Mists" by using the Copper Lantern portion of our logo prominently on our current labels. The goal is to have customers know our product when they just see the diamond and not need to read our name to know its a Copper Lantern Premium E-Liquid.

We carry 50 different flavors that each come in 5 sizes. Additionally each size comes in 4 different levels of nicotine strength (0 mg, 6 mg, 12 mg, and 18 mg) Due to label cost runs we need to put each nicotine strengths on the label with a "checkbox" system next to them so we can manually mark the correct mg strength on each bottle after applying the label.

The labels should include the following:

1- The Copper Lantern in our logo as the focal point
2- The name "Copper Lantern Mists" in our logo font Trajan Bold Pro
3- The words "Premium E-Liquid"
4- The name of the Premium E-Liquid. We have 50 flavors (please see attached flavor grid with the shortest name being "Kiwi" and the longest being "Banana Cream Menthol")
5- The following text "Caution: This product contains Nicotine. Keep out of the reach of children and pets. Do not drink. Not for sale to minors.
6- The following text "Ingredients: Propylene Glycol (USP),Glycerin (USP), L-Nicotine, FEMA/GRAS approved Natural and Artificial Flavorings. All ingredients are FDA approved for human consumption.
7- Some type of checkbox set up to mark whether the juice has "0 mg", "6 mg", "12 mg", or "18 mg" of nicotine

Although the same design will be used across all bottle sizes. We will need to make sure that the design gets a finished version in all 5 sizes.

There are 5 sizes of labels:

1- 15 ml squeeze is 2 3/4" wide x 1 5/8" high
2- 30 ml squeeze is 3 1/2" wide x 1 3/4" high
3- 15 ml glass is 3" wide x 1 1/4" high
4- 30 ml glass is 3 5/8" wide x 1 1/2" high
5- 60 ml glass is 4 5/8" wide x 1 3/4" high

Colors
0455a3
3176b5
85acd3
ceddec
0692cd
33a6d7
85cae6
cee9f5

```html
<!DOCTYPE html>
<html lang="en">
<head>
<meta charset="utf-8">
<title>Copper Lantern Mists – Strawberry Label</title>
<link rel="stylesheet" href="https://fonts.googleapis.com/css2?family=Cinzel:wght@600&family=Jost:wght@300&family=Roboto+Condensed:wght@700&display=swap">
<style>
  :root {
    --brand-blue: #0455a3;
    --ink-blue: #1b54a0;
    --label-white: #ffffff;
    --backdrop: #dcdcde;
  }
  * { box-sizing: border-box; margin: 0; padding: 0; }
  html, body {
    width: 1200px;
    height: 900px;
    overflow: hidden;
    background: var(--backdrop);
  }
  .label {
    position: absolute;
    left: 150px;
    top: 225px;
    width: 898px;
    height: 449px;
    background: var(--label-white);
    color: var(--ink-blue);
  }
  .info-column {
    position: absolute;
    left: 27px;
    top: 28px;
    width: 180px;
    font-family: "Roboto Condensed", "Arial Narrow", sans-serif;
    font-weight: 700;
    font-size: 17.5px;
    line-height: 23.5px;
    color: var(--ink-blue);
  }
  .info-column h2 {
    font: inherit;
    text-decoration: underline;
    text-underline-offset: 2px;
  }
  .info-block + .info-block { margin-top: 23px; }

  .brand-mark {
    position: absolute;
    left: 375px;
    top: 28px;
    width: 150px;
    height: 150px;
    border-radius: 50%;
    background: var(--brand-blue);
  }
  .brand-name {
    position: absolute;
    left: 300px;
    top: 216px;
    width: 300px;
    text-align: center;
    font-family: "Cinzel", "Trajan Pro", serif;
    font-weight: 600;
    font-size: 26px;
    line-height: 34px;
    letter-spacing: 3px;
    text-transform: uppercase;
    color: var(--brand-blue);
  }
  .flavor-band {
    position: absolute;
    left: 225px;
    top: 293px;
    width: 449px;
    height: 91px;
    background: var(--brand-blue);
    display: flex;
    align-items: center;
    justify-content: center;
  }
  .flavor-name {
    font-family: "Jost", "Futura", sans-serif;
    font-weight: 300;
    font-size: 37px;
    letter-spacing: 3px;
    color: var(--label-white);
    text-transform: uppercase;
  }
  .product-line {
    position: absolute;
    left: 225px;
    top: 393px;
    width: 449px;
    text-align: center;
    font-family: "Cinzel", "Trajan Pro", serif;
    font-weight: 600;
    font-size: 25px;
    letter-spacing: 4px;
    text-transform: uppercase;
    color: var(--brand-blue);
  }
  .net-weight {
    position: absolute;
    left: 715px;
    top: 329px;
    font-family: "Roboto Condensed", "Arial Narrow", sans-serif;
    font-weight: 700;
    font-size: 26px;
    color: var(--brand-blue);
  }
</style>
</head>
<body>
  <main class="label">
    <section class="info-column">
      <div class="info-block caution">
        <h2>CAUTION</h2>
        <p>This product contains<br>Nicotine. Keep out of<br>reach of children and<br>pets. Do not drink.<br>Not for sale to minors.</p>
      </div>
      <div class="info-block ingredients">
        <h2>INGREDIENTS</h2>
        <p>Propylene Glycol<br>(USP), Glycerin (USP),<br>L-Nicotine, FEMA/<br>GRAS approved<br>Natural and Artificial<br>Flavorings. All<br>ingredients are FDA<br>approved for human<br>consumption.</p>
      </div>
    </section>

    <div class="brand-mark" aria-hidden="true"></div>
    <h1 class="brand-name">Copper Lantern<br>Mists</h1>

    <div class="flavor-band">
      <span class="flavor-name">Strawberry</span>
    </div>

    <p class="product-line">Premium E-Liquid</p>

    <p class="net-weight">NET WT: 30ml</p>
  </main>
</body>
</html>
```